Business Card Design

I have a very clear idea of what I want. I just do not know how to do the graphic design to match it.

On the front I want the uploaded image with the horse and the two people.
I want

Bottom left hand corner
Lewis Brand
0438 512 607

Bottom right
There is maroon block with Neil Patton Practitioner Group Logo
Next to that I want the Stable Arc tile about the same size ( attached psd file)

On the back I want a plain colour (white) with the information

Lewis Brand
Equine Performance
Rowland4Ponies and Acupuncture
Horsemanship Lessons and Clinics
Horse Training

lbrand@fauna812.com.au
FB/lewis.brand.207
StableArc.com.au

Industry/Entity Type

Business

Contact Information for Business Card

Lewis Brand
0438 512 607
lbrand@fauna812.com.au

```html
<!DOCTYPE html>
<html lang="en">
<head>
<meta charset="utf-8">
<title>Lewis Brand – Business Card Back</title>
<link rel="stylesheet" href="https://fonts.googleapis.com/css2?family=Cinzel:wght@400;600;700&display=swap">
<style>
  :root {
    --card-bg: #ffffff;
    --ink: #000000;
  }
  html, body {
    margin: 0;
    padding: 0;
    width: 1200px;
    height: 741px;
    overflow: hidden;
    background: var(--card-bg);
  }
  .card-back {
    position: relative;
    width: 1200px;
    height: 741px;
    background: var(--card-bg);
    color: var(--ink);
    font-family: "Cinzel", serif;
    text-align: center;
  }
  .card-back p {
    position: absolute;
    left: 0;
    right: 0;
    margin: 0;
    line-height: 1;
    white-space: nowrap;
    letter-spacing: 0.05em;
  }
  .holder-name {
    top: 114px;
    font-size: 60px;
    font-weight: 700;
  }
  .service {
    font-size: 46px;
    font-weight: 400;
  }
  .service--performance { top: 194px; }
  .service--therapy     { top: 259px; }
  .service--lessons     { top: 325px; }
  .service--training    { top: 388px; }
  .contact-email {
    top: 527px;
    font-size: 52px;
    font-weight: 700;
  }
  .contact-social {
    top: 597px;
    font-size: 50px;
    font-weight: 400;
  }
  .contact-web {
    top: 659px;
    font-size: 50px;
    font-weight: 400;
  }
</style>
</head>
<body>
  <main class="card-back">
    <p class="holder-name">Lewis Brand</p>
    <p class="service service--performance">Equine Performance</p>
    <p class="service service--therapy">Rowland4Ponies and Acupuncture</p>
    <p class="service service--lessons">Horsemanship Lessons and Clinics</p>
    <p class="service service--training">Horse Training</p>
    <p class="contact-email">lbrand@fauna812.com.au</p>
    <p class="contact-social">FB/lewis.brand.207</p>
    <p class="contact-web">StableArc.com.au</p>
  </main>
</body>
</html>
```